Make us a new business / visiting cards

Please design us a new business / visiting cards.
The card must have 85 x 55 mm and should be in printing quality.
We added our company font (see attachment) and our company color is #fe6e00

Please include our logo (see attachment) and the following information on your submit.

#####################
Eines der renommiertesten Nachhilfeinstitutein Linz
Morgentalgasse 17 4021 Steinau-Nord
kontakt@lernwerk-brunnfeld.at
0664 / 38 215 904

```html
<!DOCTYPE html>
<html lang="de">
<head>
<meta charset="utf-8">
<title>Lernwerk Brunnfeld – Visitenkarte</title>
<link href="https://fonts.googleapis.com/css2?family=Oswald:wght@400;500;600&display=swap" rel="stylesheet">
<style>
  :root {
    --backdrop: #2b2b2b;
    --brand-orange: #f28a27;
    --ink-dark: #231f20;
    --paper-white: #ffffff;
    --text-light: #f4f4f4;
  }
  * { margin: 0; padding: 0; box-sizing: border-box; }
  html, body {
    width: 1200px; height: 1200px; overflow: hidden;
    background: var(--backdrop);
    font-family: "Oswald", "Arial Narrow", sans-serif;
  }
  .card {
    position: absolute;
    left: 237px; width: 726px;
    border-radius: 20px;
    overflow: hidden;
    background: var(--brand-orange);
  }
  .card--front { top: 123px; height: 414px; }
  .card--back { top: 595px; height: 410px; }

  .wordmark {
    position: absolute; left: 0; right: 0;
    display: flex; align-items: center; justify-content: center; gap: 18px;
    color: var(--ink-dark);
    font-weight: 600; letter-spacing: 3px; text-transform: uppercase;
  }
  .wordmark__square { width: 34px; height: 34px; background: var(--ink-dark); }
  .card--front .wordmark { top: 170px; font-size: 50px; line-height: 70px; }
  .card--back .wordmark { top: 66px; font-size: 44px; line-height: 62px; }
  .card--back .wordmark__square { width: 30px; height: 30px; }

  .info-band {
    position: absolute; left: 0; right: 0; top: 232px; bottom: 0;
    background: var(--ink-dark);
    border-top: 4px solid var(--paper-white);
  }
  .identity {
    position: absolute; right: 380px; top: 50px;
    text-align: right; color: var(--text-light);
    white-space: nowrap;
  }
  .identity__name { font-size: 24px; font-weight: 500; line-height: 32px; }
  .identity__role { font-size: 15px; color: var(--brand-orange); line-height: 26px; }
  .identity__address { font-size: 17px; line-height: 26px; }
  .divider {
    position: absolute; left: 370px; top: 48px; width: 2px; height: 84px;
    background: var(--brand-orange);
  }
  .contacts { position: absolute; left: 394px; top: 46px; list-style: none; }
  .contacts li {
    display: flex; align-items: center; gap: 10px;
    height: 30px; font-size: 18px; color: var(--text-light);
    white-space: nowrap;
  }
  .contacts svg { width: 18px; height: 18px; flex: none; }
</style>
</head>
<body>
  <section class="card card--front">
    <div class="wordmark"><span class="wordmark__square"></span>Lernwerk Brunnfeld</div>
  </section>

  <section class="card card--back">
    <div class="wordmark"><span class="wordmark__square"></span>Lernwerk Brunnfeld</div>
    <div class="info-band">
      <div class="identity">
        <p class="identity__name">NACHHILFE STEINAU</p>
        <p class="identity__role">Founder/CEO</p>
        <p class="identity__address">Morgentalgasse 17 4021 Steinau-Nord</p>
      </div>
      <span class="divider"></span>
      <ul class="contacts">
        <li>
          <svg viewBox="0 0 24 24" aria-hidden="true"><path fill="#f28a27" d="M6.6 10.8a15.1 15.1 0 0 0 6.6 6.6l2.2-2.2c.3-.3.7-.4 1-.2 1.1.4 2.3.6 3.6.6.6 0 1 .4 1 1V20c0 .6-.4 1-1 1A17 17 0 0 1 3 4c0-.6.4-1 1-1h3.5c.6 0 1 .4 1 1 0 1.3.2 2.5.6 3.6.1.3 0 .7-.2 1z"/></svg>
          0664 / 38 215 904
        </li>
        <li>
          <svg viewBox="0 0 24 24" aria-hidden="true"><rect x="2" y="5" width="20" height="14" fill="#f28a27"/><path d="M2 5l10 8 10-8" fill="none" stroke="#231f20" stroke-width="2"/></svg>
          kontakt@lernwerk-brunnfeld.at
        </li>
        <li>
          <svg viewBox="0 0 24 24" aria-hidden="true"><g fill="none" stroke="#f28a27" stroke-width="2"><circle cx="12" cy="12" r="9"/><ellipse cx="12" cy="12" rx="4" ry="9"/><path d="M3 12h18M5 7h14M5 17h14"/></g></svg>
          www.lernwerk-brunnfeld.at
        </li>
      </ul>
    </div>
  </section>
</body>
</html>
```